Business Card Design Project

Require a business card for a swing band called "Velvet Brass Parade". We are a 6 piece band that performs at events and corporate functions. Our music is great for dancing to or just providing a classy background atmosphere for people to enjoy. Final design should communicate professionalism and style with a hint of fun.

Sorry, just realised that it needs to be single sided only. Also, no rounded edges.

Industry/Entity Type

Events

Requirements
Must have
• Contact number: 0438 216 903
email address: velvetbrassparade@mailbox-demo.net
Website details: www.velvetbrassparade-demo.com

```html
<!DOCTYPE html>
<html lang="en">
<head>
<meta charset="utf-8">
<title>Velvet Brass Parade – Business Card</title>
<link rel="stylesheet" href="https://fonts.googleapis.com/css2?family=Pinyon+Script&family=PT+Sans&display=swap">
<style>
  :root {
    --card-cream: #fdf3c9;
    --name-brown: #2e2219;
    --contact-red: #b3203a;
    --note-orange: #ee7a2c;
    --note-purple: #7b2a86;
    --note-red: #d42a2f;
    --note-magenta: #e0198a;
    --note-green: #3f6b4c;
  }
  * { margin: 0; padding: 0; box-sizing: border-box; }
  html, body {
    width: 754px;
    height: 1200px;
    overflow: hidden;
    background: var(--card-cream);
  }
  .business-card {
    position: relative;
    width: 754px;
    height: 1200px;
    background: var(--card-cream);
    overflow: hidden;
  }
  .music-illustration {
    position: absolute;
    top: 0;
    left: 0;
    width: 754px;
    height: 470px;
  }
  .band-name {
    position: absolute;
    left: 0;
    top: 0;
    width: 754px;
    height: 820px;
    font-family: "Pinyon Script", cursive;
    font-weight: 400;
    color: var(--name-brown);
    line-height: 1;
  }
  .band-name span { display: block; position: absolute; white-space: nowrap; }
  .band-name .word-velvet { left: 100px; top: 445px; font-size: 160px; }
  .band-name .word-brass  { left: 205px; top: 700px; font-size: 46px; }
  .band-name .word-parade { left: 345px; top: 610px; font-size: 136px; }
  .contact-details {
    position: absolute;
    left: 0;
    top: 1000px;
    width: 754px;
    text-align: center;
    font-family: "PT Sans", sans-serif;
    font-size: 33px;
    line-height: 48px;
    color: var(--contact-red);
    list-style: none;
  }
</style>
</head>
<body>
<main class="business-card">
  <svg class="music-illustration" viewBox="0 0 754 470">
    <defs>
      <linearGradient id="notes-tones" x1="0" y1="0" x2="1" y2="1">
        <stop offset="0" stop-color="var(--note-orange)"/>
        <stop offset="0.3" stop-color="var(--note-purple)"/>
        <stop offset="0.5" stop-color="var(--note-red)"/>
        <stop offset="0.7" stop-color="var(--note-magenta)"/>
        <stop offset="1" stop-color="var(--note-green)"/>
      </linearGradient>
    </defs>
    <path role="img"
          aria-label="Colourful musical notes, a treble clef and a bass clef dancing along a diagonal music staff"
          d="M150 20 L560 20 L740 230 L740 450 L600 400 L420 360 L200 230 Z"
          fill="url(#notes-tones)" opacity="0.55"/>
  </svg>

  <h1 class="band-name" aria-label="Velvet Brass Parade">
    <span class="word-velvet">Velvet</span>
    <span class="word-brass">Brass</span>
    <span class="word-parade">Parade</span>
  </h1>

  <ul class="contact-details">
    <li class="contact-phone">0438 216 903</li>
    <li class="contact-email">velvetbrassparade@mailbox-demo.net</li>
    <li class="contact-web">www.velvetbrassparade-demo.com</li>
  </ul>
</main>
</body>
</html>
```